Harborline Safety Courses

I'm currently in the process of setting up a First Aid and Lifeguard Training website. The project has already began through a web designer but he is unable to meet the deadline.
There's is already a landing page
http://www.harborlinesafetycourses.example.au/
In addition he also started to create the website
https://mockups.example.net/view/9c41d7e0-5b2a-4e8f-a613-d02e7bb18c39-2218/?fullscreen
The home page ideally needs to have a different visual and user journey from the quick landing page created
- The Logo in the top left hand corner looks a bit out of whack, maybe it needs to be bigger ??
-The tabs along the top need to be 'designed' and spaced out equally: home, about, courses, contact, gallery. Can we please remove Accredited First Aid and Lifeguard.
-the blue bar with the tag line needs to be redesigned - that was ok for a landing page but not quite right for actual website, it looks clunky
-all the course info needs to be placed under the courses tab not on the home page. I would like a roll down bar ( Check out Tidewater Rescue Aid website on their First Aid Course) so the client can book a date and proceed to the checkout basket. I will supply those soon; this will only apply to the Provide First Aid and Provide Cardiopulmonary Resuscitation Courses.
- The rest of the courses can have an enquire option
-the about paragraphs need to go directly under banner
-then a rolling slider with upcoming courses - with each course, rolling to give the home page some pop
- followed by pictures/ images of recent courses linked to gallery page updates or social feed
-remove newsletter
In addition to this I also have a logo designed via sketch harbor and lots of photos as well as briefs on all the courses that I will offer.
Accredited First Aid and CPR Courses. Lifeguard and Community Safety Programs Programs

```html
<!DOCTYPE html>
<html lang="en">
<head>
<meta charset="utf-8">
<title>Harborline Safety Courses — Home</title>
<link rel="stylesheet" href="https://fonts.googleapis.com/css2?family=Ubuntu:wght@500;700&family=Roboto:ital,wght@0,300;0,400;0,500;0,700;1,400;1,500&display=swap">
<style>
:root{
  --blue:#2f8fcf;
  --blue-deep:#1f6fb3;
  --navy:#0d2a4a;
  --orange:#f07a1a;
  --pale:#e5f0fa;
  --ink:#222;
  --muted:#666;
  --white:#fff;
}
*{box-sizing:border-box;margin:0;padding:0}
html,body{width:1200px;height:3174px;overflow:hidden;background:var(--white)}
body{position:relative;font-family:"Roboto",sans-serif;color:var(--ink)}
.abs{position:absolute}

/* header */
.site-header{position:absolute;left:0;top:0;width:1200px;height:96px;background:var(--white);z-index:5}
.brand-plate{position:absolute;left:142px;top:-8px;width:190px;height:190px;border-radius:50%;background:var(--white);z-index:6;display:flex;align-items:center;justify-content:center;text-align:center}
.brand-name{font-family:"Ubuntu",sans-serif;font-weight:700;font-size:21px;line-height:1.15;color:var(--blue);width:140px}
.main-nav{position:absolute;left:460px;top:0;display:flex;height:102px}
.main-nav a{font-family:"Roboto",sans-serif;font-weight:500;font-size:14px;color:#111;text-decoration:none;display:flex;align-items:center;height:96px;padding:0 20px}
.main-nav a.is-active{background:var(--blue);color:var(--white);height:102px;padding:0 21px}
.header-icons{position:absolute;left:950px;top:36px;display:flex;gap:18px}

/* hero */
.hero-photo{position:absolute;left:0;top:0;width:1200px;height:790px;background:linear-gradient(135deg,#0f4fa0 0%,#1f7ad4 45%,#2a8ee0 70%,#174f9a 100%)}
.hero-title{position:absolute;left:145px;top:254px;font-family:"Ubuntu",sans-serif;font-weight:700;font-size:47px;line-height:53px;color:var(--white);text-transform:uppercase;text-shadow:0 2px 4px rgba(0,0,0,.35)}
.slide-dots{position:absolute;left:1145px;top:608px}
.slide-dots span{display:block;width:8px;height:8px;border-radius:50%;background:var(--white);margin-bottom:8px}
.slide-dots span.is-current{background:var(--orange)}
.wave{position:absolute;left:0;display:block}

/* welcome */
.section-title{position:absolute;left:0;width:1200px;text-align:center;font-family:"Ubuntu",sans-serif;font-weight:700;color:var(--navy)}
.welcome-copy{position:absolute;left:190px;top:832px;width:820px;text-align:center;font-size:15.5px;line-height:26.5px;color:var(--muted);font-weight:300}
.welcome-copy p+p{margin-top:26px}
.rto-line{position:absolute;left:0;top:1052px;width:1200px;text-align:center;font-size:24px;font-weight:500;color:var(--blue)}
.btn{display:inline-flex;align-items:center;justify-content:center;border-radius:40px;color:var(--white);font-weight:500;text-transform:uppercase;text-decoration:none}
.btn-orange{background:var(--orange)}
.btn-blue{background:var(--blue)}
.welcome-cta{position:absolute;left:498px;top:1128px;width:205px;height:73px;font-size:19px}

/* courses */
.courses-band{position:absolute;left:0;top:1190px;width:1200px;height:940px;background:var(--pale)}
.course-card{position:absolute;top:1486px;width:447px;height:538px;background:var(--white);box-shadow:0 2px 6px rgba(0,0,0,.12)}
.course-photo{height:223px}
.course-body{padding:28px 37px 0}
.course-name{font-size:15.5px;font-weight:500;line-height:24px;color:#111;height:48px;text-transform:uppercase}
.course-tag{margin-top:13px;font-size:13px;color:var(--blue);text-transform:uppercase}
.course-facts{margin-top:18px;list-style:none;font-size:13px;line-height:24px;color:#222;padding-left:2px}
.course-facts b{font-weight:700}
.course-actions{margin-top:19px;display:flex;gap:7px}
.course-actions .btn{width:167px;height:59px;font-size:15.5px}
.round-arrow{position:absolute;width:45px;height:45px;border-radius:50%;border:1.5px solid #555;display:flex;align-items:center;justify-content:center}

/* gallery */
.gallery-strip{position:absolute;left:0;top:2125px;width:1200px;height:352px;display:flex;gap:3px}
.gallery-strip div{flex:1}
.gallery-arrow{position:absolute;top:2317px;width:30px;height:52px;background:#1a1a1a;display:flex;align-items:center;justify-content:center}

/* testimonial */
.testimonial-quote{position:absolute;left:0;top:2646px;width:1200px;text-align:center;font-style:italic;font-size:22px;line-height:34.5px;color:#222}
.testimonial-author{position:absolute;left:0;top:2782px;width:1200px;text-align:center;font-size:24px;font-weight:500;color:var(--blue)}
.testimonial-author em{color:var(--orange);font-weight:400}

/* footer */
.site-footer{position:absolute;left:0;top:2800px;width:1200px;height:374px}
.footer-contact{position:absolute;left:427px;top:3003px;font-size:20px;font-weight:500;color:var(--white);display:flex;align-items:center;gap:8px}
.footer-nav{position:absolute;left:427px;top:3060px;font-size:15.5px;font-weight:500;color:var(--white);text-transform:uppercase;word-spacing:6px}
.copyright{position:absolute;left:427px;top:3104px;font-size:11px;color:var(--white)}
.footer-brand{position:absolute;left:184px;top:2985px;width:160px;height:160px;border-radius:50%;border:2px solid var(--white);display:flex;align-items:center;justify-content:center;text-align:center}
.footer-brand span{font-family:"Ubuntu",sans-serif;font-weight:700;font-size:18px;line-height:1.15;color:var(--white);width:120px}
</style>
</head>
<body>

<!-- hero -->
<div class="hero-photo" role="img" aria-label="Photo: instructors standing in an empty blue pool around a person lying beside a yellow rescue stretcher"></div>
<h1 class="hero-title">Accredited<br>training from<br>first aid to<br>lifeguard<br>programs</h1>
<div class="slide-dots"><span></span><span class="is-current"></span><span></span><span></span></div>

<svg class="wave" style="top:600px" width="1200" height="200" viewBox="0 0 1200 200">
  <path d="M0 130 Q600 -20 1200 110 L1200 200 L0 200 Z" fill="#1f6fb3"/>
  <path d="M0 145 Q600 10 1200 125 L1200 200 L0 200 Z" fill="#fff"/>
  <path d="M0 152 Q600 20 1200 132" fill="none" stroke="#2f8fcf" stroke-width="9"/>
  <path d="M0 172 Q600 50 1200 160 L1200 200 L0 200 Z" fill="#fff"/>
  <circle cx="601" cy="49" r="42" fill="#fff"/>
</svg>

<!-- header -->
<header class="site-header">
  <nav class="main-nav">
    <a class="is-active" href="#">HOME</a>
    <a href="#">ABOUT</a>
    <a href="#">COURSES</a>
    <a href="#">CONTACT</a>
    <a href="#">GALLERY</a>
  </nav>
  <div class="header-icons">
    <svg width="24" height="24" viewBox="0 0 24 24"><circle cx="10" cy="10" r="7" fill="none" stroke="#2f8fcf" stroke-width="3"/><path d="M15 15l7 7" stroke="#2f8fcf" stroke-width="3.5" stroke-linecap="round"/></svg>
    <svg width="24" height="24" viewBox="0 0 24 24"><path d="M1 3h4l3 12h12l3-9H7" fill="none" stroke="#f07a1a" stroke-width="2.5"/><path d="M8 7h14l-2 7H9z" fill="#f07a1a"/><circle cx="9" cy="20" r="2" fill="#f07a1a"/><circle cx="19" cy="20" r="2" fill="#f07a1a"/></svg>
    <svg width="22" height="24" viewBox="0 0 22 24"><circle cx="11" cy="7" r="6" fill="#2f8fcf"/><path d="M0 24c0-7 5-10 11-10s11 3 11 10z" fill="#2f8fcf"/></svg>
  </div>
</header>
<div class="brand-plate"><span class="brand-name">Harborline Safety Courses</span></div>

<!-- welcome -->
<h2 class="section-title" style="top:750px;font-size:47px">WELCOME</h2>
<div class="welcome-copy">
  <p>Harborline Safety Courses delivers a series of Emergency training accreditation and innovative general safety awareness programs. From general first aid to Lifeguard training courses, our carefully designed training methods ensure all students leave with clarity and confidence in managing emergency scenarios.</p>
  <p>At Harborline, we ensure impactful training programs are delivered through skillfully creating methodologies that are clear and memorable. We bring a huge realm of emergency story telling into our courses which create a high energy, engaging and positive learning experience. Our programs truly bring out the “Calm Responder” in those who attend.</p>
</div>
<p class="rto-line">Training and Assessment delivered on behalf of Corvane Pty Ltd (RTO #00000)</p>
<a class="btn btn-orange welcome-cta" href="#">ENQUIRE NOW</a>

<!-- upcoming courses -->
<div class="courses-band"></div>
<svg class="wave" style="top:1189px" width="1200" height="110" viewBox="0 0 1200 110"><path d="M0 0 H1200 V4 Q600 204 0 4 Z" fill="#fff"/></svg>
<h2 class="section-title" style="top:1382px;font-size:47px">UPCOMING COURSES</h2>

<article class="course-card" style="left:144px">
  <div class="course-photo" role="img" aria-label="Photo: lifeguard trainees in blue hoodies on a beach with an instructor" style="background:linear-gradient(180deg,#4f6e96 0%,#6f8aa6 45%,#c9b89a 75%,#d8c7a8 100%)"></div>
  <div class="course-body">
    <h3 class="course-name">Provide Cardiopulmonary Resuscitation HLTAID009</h3>
    <p class="course-tag">Limited places</p>
    <ul class="course-facts">
      <li><b>Cost:</b> $60.00</li>
      <li><b>Time:</b> 10.30am-12.30</li>
      <li><b>Venue:</b> Stillwater Yoga Studio, Kiama</li>
      <li><b>Reserve your place:</b> bookings@harborlinesafety.example.au</li>
    </ul>
    <div class="course-actions"><a class="btn btn-orange" href="#">ENQUIRE NOW</a><a class="btn btn-blue" href="#">BOOK NOW</a></div>
  </div>
</article>

<article class="course-card" style="left:609px">
  <div class="course-photo" role="img" aria-label="Photo: trainees in an empty blue pool practising a stretcher rescue" style="background:linear-gradient(160deg,#0d3f9e 0%,#1d62c4 50%,#7fa0d0 80%,#1b4fa8 100%)"></div>
  <div class="course-body">
    <h3 class="course-name">Provide First Aid HLTAID011</h3>
    <p class="course-tag">Limited places</p>
    <ul class="course-facts">
      <li><b>Cost:</b> $60.00</li>
      <li><b>Time:</b> 10.30am-12.30</li>
      <li><b>Venue:</b> Stillwater Yoga Studio, Kiama</li>
      <li><b>Reserve your place:</b> bookings@harborlinesafety.example.au</li>
    </ul>
    <div class="course-actions"><a class="btn btn-orange" href="#">ENQUIRE NOW</a><a class="btn btn-blue" href="#">BOOK NOW</a></div>
  </div>
</article>

<div class="round-arrow" style="left:72px;top:1733px"><svg width="14" height="20" viewBox="0 0 14 20"><path d="M11 2L3 10l8 8" fill="none" stroke="#333" stroke-width="2.2"/></svg></div>
<div class="round-arrow" style="left:1083px;top:1733px"><svg width="14" height="20" viewBox="0 0 14 20"><path d="M3 2l8 8-8 8" fill="none" stroke="#333" stroke-width="2.2"/></svg></div>

<!-- recent course gallery -->
<div class="gallery-strip">
  <div role="img" aria-label="Photo: students practising CPR on training manikins" style="background:linear-gradient(135deg,#5c7fa0,#b9a38a 55%,#7a5c48)"></div>
  <div role="img" aria-label="Photo: large group of course participants in hi-vis bibs with manikins" style="background:linear-gradient(180deg,#4a5c7a,#7ea0c8 40%,#a8c83c 70%,#8a6e5a)"></div>
  <div role="img" aria-label="Photo: instructor in a lifeguard shirt holding a defibrillator pad" style="background:linear-gradient(135deg,#7a4e2c,#c08454 40%,#3aa9c9 75%,#1e4b6e)"></div>
  <div role="img" aria-label="Photo: lifeguard trainees on a beach beside an all-terrain vehicle" style="background:linear-gradient(180deg,#6aa2d8,#2c5a3a 35%,#d8c6a4 60%,#c9b48e)"></div>
</div>
<svg class="wave" style="top:2124px" width="1200" height="40" viewBox="0 0 1200 40"><path d="M0 0 H1200 V32 Q900 -2 600 0 Q300 -2 0 32 Z" fill="#e5f0fa"/></svg>
<div class="gallery-arrow" style="left:0"><svg width="10" height="16" viewBox="0 0 10 16"><path d="M8 2L2 8l6 6" fill="none" stroke="#fff" stroke-width="2"/></svg></div>
<div class="gallery-arrow" style="left:1170px"><svg width="10" height="16" viewBox="0 0 10 16"><path d="M2 2l6 6-6 6" fill="none" stroke="#fff" stroke-width="2"/></svg></div>

<!-- testimonial -->
<svg class="abs" style="left:568px;top:2554px" width="64" height="60" viewBox="0 0 64 60">
  <path d="M32 4C16 4 4 13 4 26c0 7 4 13 10 17l-4 13 14-9c2 .4 5 .6 8 .6 16 0 28-9 28-21S48 4 32 4z" fill="none" stroke="#2f8fcf" stroke-width="3"/>
  <path d="M20 22a5 5 0 1 1 2 9c0 3-2 5-5 6 2-2 3-4 2-6-2-1-3-3-1-6zM36 22a5 5 0 1 1 2 9c0 3-2 5-5 6 2-2 3-4 2-6-2-1-3-3-1-6z" fill="#2f8fcf"/>
</svg>
<p class="testimonial-quote">Lorem ipsum dolor sit amet, consectetur adipiscing elit, sed do eiusmod tempor<br>incididunt ut labore et dolore magna aliquauis ipsum suspendisse ultrices gravida.<br>Risus commodo viverra maecenas accumsan lacus vel facilisis.</p>
<p class="testimonial-author">- John Doe,<em>Customer</em></p>
<svg class="abs" style="left:114px;top:2710px" width="36" height="66" viewBox="0 0 36 66"><path d="M34 1L2 33l32 32" fill="none" stroke="#777" stroke-width="1.2"/></svg>
<svg class="abs" style="left:1050px;top:2710px" width="36" height="66" viewBox="0 0 36 66"><path d="M2 1l32 32L2 65" fill="none" stroke="#777" stroke-width="1.2"/></svg>

<!-- footer -->
<footer class="site-footer">
  <svg class="wave" style="top:0" width="1200" height="374" viewBox="0 0 1200 374">
    <path d="M0 0 Q600 160 1200 20 L1200 374 L0 374 Z" fill="#1f6fb3"/>
    <path d="M0 14 Q600 174 1200 34 L1200 374 L0 374 Z" fill="#2f8fcf"/>
    <path d="M0 36 Q600 190 1200 56" fill="none" stroke="#fff" stroke-width="4"/>
    <circle cx="601" cy="116" r="42" fill="#fff"/>
  </svg>
  <div class="footer-brand"><span>Harborline Safety Courses</span></div>
  <div class="footer-contact">
    <svg width="20" height="20" viewBox="0 0 24 24"><path d="M6 2l4 5-2 3c1 3 3 5 6 6l3-2 5 4-3 4C10 22 2 14 2 5z" fill="#fff"/></svg>
    <span>0400 555 182</span><span style="margin:0 10px">|</span>
    <svg width="22" height="18" viewBox="0 0 22 18"><rect x="1" y="1" width="20" height="16" rx="2" fill="#fff"/><path d="M1 3l10 7 10-7" fill="none" stroke="#2f8fcf" stroke-width="2"/></svg>
    <span>bookings@harborlinesafety.example.au</span>
  </div>
  <nav class="footer-nav">HOME &nbsp;/&nbsp; ABOUT &nbsp;/&nbsp; COURSES &nbsp;/&nbsp; CONTACT &nbsp;/&nbsp; GALLERY</nav>
  <p class="copyright">© Copyright 2021 Harborline Safety Courses.All Rights Reserved &nbsp;|&nbsp; Privacy Policy</p>
</footer>

</body>
</html>
```